Lanterns on the Tide

I need a book cover design for a world history book written for a target audience of high school students and progressive teachers. The book is more balanced towards a world history perspective than a Western-leaning perspective. The first 500 pages deal with the major turning points in world history - from the first hominids that roamed Africa to the end of the Cold War, and the final 100 pages cover the major challenges facing the world today. The book is 95% graphic details, hopefully-engaging stories and needed facts, but there is a bit of sarcasm, verbal irony and asides thrown in to keep the reader's eyes from glossing over. I would need a cover that would appeal to any school teacher, but something that would not scare off students or the average Joe off the street.
Updates

One added note, please leave the bottom right corner -  2" height by 3" width free of text/image for the ISBN code.

As far as a central image goes, it needs to be a dynamic (avoid something readers would readily see elsewhere in their lives) image, or nothing at all.  Also, please justify all text on the back cover to the left side (avoid centering).

Reason: A few people have voiced an interest in having the deadline extended through next weekend to allow for some alterations and also the ability to take advantage of the upcoming holidays. I will take you up on this request. Thank you all again for your submissions. i've seen some very unique takes on the story/tone of the book.

Industry/Entity Type

High School

Requirements
Must have
• I've enclosed a PDF with the text for the front and back cover.

On the back cover, I'd like the quote and the initial question to stand out. I'd like the initial question to be in lower case.

For the spine, I'd like the title font to match the title front from the front cover.

The book cover needs to measure 9.25" by 13.75" with a 1.5" spine. Allow .125 inches for the bleed.

I've attached a Word Document with all the text. The layout is just a suggestion.
Should not have
• I do not want any stock images that I'll need to pay for.

```html
<!DOCTYPE html>
<html lang="en">
<head>
<meta charset="utf-8">
<title>Lanterns on the Tide — Full Cover</title>
<link rel="stylesheet" href="https://fonts.googleapis.com/css2?family=Alegreya:ital,wght@0,400;0,500;1,400&display=swap">
<style>
  :root {
    --page-bg: #f2f2f2;
    --sky-top: #5f9aa3;
    --sky-mid: #3f8590;
    --sky-low: #2d7380;
    --field-top: #4a6a4a;
    --field-low: #1d2a20;
    --title-red: #a8483a;
    --title-white: #f4f1ea;
    --text-white: #eef0ec;
    --text-soft: #d9e6e6;
    --heart-light: #e6cfc9;
    --heart-mid: #c9a09a;
    --heart-shadow: #8e6a66;
    --debris-light: #b9c2c4;
    --debris-dark: #3c4a4c;
    --isbn-box: #ffffff;
    --spine-edge: rgba(0, 0, 0, 0.18);
  }

  * { box-sizing: border-box; margin: 0; padding: 0; }

  html, body {
    width: 1200px;
    height: 1200px;
    overflow: hidden;
    background: var(--page-bg);
  }

  .canvas {
    width: 1200px;
    height: 1200px;
    display: flex;
    align-items: center;
    justify-content: center;
  }

  .cover-spread {
    display: flex;
    width: 1140px;
    height: 768px;
    font-family: "Alegreya", Georgia, serif;
  }

  .panel {
    position: relative;
    height: 100%;
    overflow: hidden;
    background:
      radial-gradient(ellipse at 30% 20%, rgba(180, 215, 215, 0.35), transparent 55%),
      radial-gradient(ellipse at 80% 55%, rgba(20, 70, 80, 0.35), transparent 60%),
      linear-gradient(180deg, var(--sky-top) 0%, var(--sky-mid) 40%, var(--sky-low) 74%, var(--field-top) 79%, var(--field-low) 100%);
  }

  .back-cover, .front-cover { width: 508px; }

  .spine {
    width: 124px;
    border-left: 1px solid var(--spine-edge);
    border-right: 1px solid var(--spine-edge);
  }

  /* Back cover */
  .back-question {
    position: absolute;
    top: 34px;
    left: 34px;
    width: 420px;
    color: var(--title-white);
    font-size: 36px;
    font-weight: 400;
    line-height: 1.1;
  }

  .back-copy {
    position: absolute;
    top: 132px;
    left: 34px;
    width: 440px;
    color: var(--text-white);
    font-size: 14px;
    line-height: 1.4;
    text-align: left;
  }

  .back-copy p + p { margin-top: 10px; }

  .back-quote {
    font-style: italic;
    font-size: 18px;
    line-height: 1.3;
    color: var(--title-white);
  }

  .back-image {
    position: absolute;
    left: 0;
    bottom: 0;
    width: 270px;
    height: 250px;
    background:
      radial-gradient(ellipse at 30% 70%, var(--debris-light), transparent 65%),
      linear-gradient(160deg, transparent 0%, var(--debris-dark) 60%, var(--field-low) 100%);
    opacity: 0.85;
  }

  .isbn-area {
    position: absolute;
    right: 30px;
    bottom: 30px;
    width: 200px;
    height: 120px;
    background: var(--isbn-box);
  }

  /* Spine */
  .spine-title {
    position: absolute;
    top: 50%;
    left: 50%;
    transform: translate(-50%, -50%) rotate(90deg);
    white-space: nowrap;
    color: var(--title-white);
    font-size: 40px;
    font-weight: 400;
    letter-spacing: 2px;
    text-transform: uppercase;
  }

  .spine-title .title-red { color: var(--title-red); }

  /* Front cover */
  .cover-title {
    position: absolute;
    top: 40px;
    left: 36px;
    font-weight: 400;
    font-size: 70px;
    line-height: 1;
    letter-spacing: 1px;
    text-transform: uppercase;
  }

  .cover-title span { display: block; }
  .title-red { color: var(--title-red); }
  .title-white { color: var(--title-white); }

  .cover-image {
    position: absolute;
    left: 228px;
    top: 300px;
    width: 190px;
    height: 250px;
    border-radius: 50% 50% 50% 50% / 38% 38% 62% 62%;
    background: radial-gradient(ellipse at 40% 35%, var(--heart-light) 0%, var(--heart-mid) 55%, var(--heart-shadow) 100%);
    box-shadow: 22px 8px 30px rgba(20, 30, 30, 0.35);
  }

  .cover-tagline {
    position: absolute;
    left: 24px;
    top: 400px;
    width: 180px;
    color: var(--text-white);
    font-size: 16px;
    line-height: 1.25;
  }

  .cover-author {
    position: absolute;
    left: 0;
    right: 0;
    bottom: 40px;
    text-align: center;
    color: var(--title-white);
    font-size: 48px;
    font-weight: 400;
    letter-spacing: 2px;
    text-transform: uppercase;
  }
</style>
</head>
<body>
  <main class="canvas">
    <div class="cover-spread">

      <section class="panel back-cover">
        <div class="back-image" role="img" aria-label="A heap of discarded bottles and plastic waste along the horizon"></div>
        <h2 class="back-question">do you have any idea how we got to here?</h2>
        <div class="back-copy">
          <p>From the first hominids walking across the African savanna to the final days of the Cold War, this book follows the turning points that shaped every region of the planet, not just the West.</p>
          <p>Along the way you will meet empires that rose and crumbled, ideas that travelled further than armies, and ordinary people who changed more than they ever expected.</p>
          <p class="back-quote">“History is not a list of dates. It is the long conversation that explains the world we wake up in.”</p>
          <p>The final chapters turn to the challenges regions face today, told with facts, stories and the occasional raised eyebrow.</p>
        </div>
        <div class="isbn-area" aria-label="Space reserved for ISBN"></div>
      </section>

      <section class="panel spine">
        <h2 class="spine-title"><span class="title-red">Lanterns</span> on the <span class="title-red">Tide</span></h2>
      </section>

      <section class="panel front-cover">
        <h1 class="cover-title">
          <span class="title-red">Lanterns</span>
          <span class="title-white">On the</span>
          <span class="title-red">Tide</span>
        </h1>
        <div class="cover-image" role="img" aria-label="A pale pink heart-shaped balloon, knotted at the bottom, resting on the horizon"></div>
        <p class="cover-tagline">The tales, traditions and turning points of world history and the regional challenges of today</p>
        <p class="cover-author">Marcus Ellery</p>
      </section>

    </div>
  </main>
</body>
</html>
```